Book cover for book of Poems "Lanternfall"

I have written a book of poems. The book is titled "Lanternfall" and has 160 pages. The poems were written mostly during my youth but there are newer poems also written over the past 10 years (I'm 42 now). They are mostly about love, loss, social conformity, and nature. I'm influenced a lot by the English Romantic Poets, gothic motives, and 80s music by bands such as The Vells, Corabel & the Tarrows, and Pennock. I need an original book cover design for my book. Attached are samples of designs I like and few of my poems. The cover will be a hardcover and I need design for Front Cover, Back Cover, and Spine. Dimension is 6"x9". Front Cover should have name of book "Lanternfall" and name of author "Ravi Menhar". Thanks.
Updates

Further details which I should have included in my original brief -The book cover will be a hard cover. Design is required for front cover, back cover, and spine. Dimension is 6x9.Front should have book title "Lanternfall" and author's name "Ravi Menhar". Added Monday, December 19, 2016

Target Market(s)

Mostly friends and family

Requirements
Must have
• I don't mind a design where lanternfall is spelled out in big capital letters and text from one of my poems is inside, like the sample I've attached.

```html
<!DOCTYPE html>
<html lang="en">
<head>
<meta charset="utf-8">
<title>Lanternfall — Ravi Menhar</title>
<link rel="stylesheet" href="https://fonts.googleapis.com/css2?family=Staatliches&display=swap">
<style>
  :root {
    --mustard: #e8ab24;
    --mustard-deep: #c98f1c;
    --ink: #111008;
  }
  html, body {
    margin: 0;
    padding: 0;
    overflow: hidden;
    background: var(--mustard);
  }
  .cover {
    position: relative;
    width: 800px;
    height: 1200px;
    overflow: hidden;
    background: var(--mustard);
  }
  .vine {
    position: absolute;
    top: 0;
  }
  .vine--left {
    left: 0;
    width: 200px;
    height: 345px;
    background: radial-gradient(ellipse at 40% 30%, rgba(17,16,8,0.55), rgba(17,16,8,0) 70%);
  }
  .vine--right {
    right: 0;
    width: 560px;
    height: 330px;
    background: radial-gradient(ellipse at 65% 20%, rgba(17,16,8,0.5), rgba(17,16,8,0) 70%);
  }
  .title-puppets {
    position: absolute;
    inset: 0;
  }
  .title-letter {
    font-family: "Staatliches", sans-serif;
    font-size: 190px;
    fill: var(--ink);
  }
  .stick {
    stroke: var(--ink);
    stroke-width: 3;
  }
  .author-plate {
    fill: var(--mustard);
  }
  .author-name {
    font-family: "Staatliches", sans-serif;
    font-size: 50px;
    letter-spacing: 2px;
    fill: var(--ink);
  }
</style>
</head>
<body>
<main class="cover">
  <div class="vine vine--left" role="img" aria-label="Black ivy vine with heart-shaped leaves hanging from the top left corner"></div>
  <div class="vine vine--right" role="img" aria-label="Black ivy vine with heart-shaped leaves trailing across the top right"></div>

  <svg class="title-puppets" width="800" height="1200" viewBox="0 0 800 1200" aria-labelledby="book-title">
    <title id="book-title">Lanternfall</title>
    <g class="sticks">
      <line class="stick" x1="38"  y1="585" x2="55"  y2="1200"/>
      <line class="stick" x1="110" y1="560" x2="125" y2="1200"/>
      <line class="stick" x1="182" y1="635" x2="170" y2="1200"/>
      <line class="stick" x1="255" y1="580" x2="262" y2="1200"/>
      <line class="stick" x1="327" y1="600" x2="318" y2="1200"/>
      <line class="stick" x1="400" y1="565" x2="405" y2="1200"/>
      <line class="stick" x1="472" y1="620" x2="462" y2="1200"/>
      <line class="stick" x1="545" y1="625" x2="548" y2="1200"/>
      <line class="stick" x1="617" y1="580" x2="610" y2="1200"/>
      <line class="stick" x1="690" y1="600" x2="705" y2="1200"/>
      <line class="stick" x1="762" y1="605" x2="770" y2="1200"/>
    </g>
    <g class="letters" aria-hidden="true">
      <text class="title-letter" x="38"  y="590" text-anchor="middle">L</text>
      <text class="title-letter" x="110" y="565" text-anchor="middle">A</text>
      <text class="title-letter" x="182" y="640" text-anchor="middle">N</text>
      <text class="title-letter" x="255" y="585" text-anchor="middle">T</text>
      <text class="title-letter" x="327" y="605" text-anchor="middle">E</text>
      <text class="title-letter" x="400" y="570" text-anchor="middle">R</text>
      <text class="title-letter" x="472" y="625" text-anchor="middle">N</text>
      <text class="title-letter" x="545" y="630" text-anchor="middle">F</text>
      <text class="title-letter" x="617" y="585" text-anchor="middle">A</text>
      <text class="title-letter" x="690" y="605" text-anchor="middle">L</text>
      <text class="title-letter" x="762" y="610" text-anchor="middle">L</text>
    </g>
    <g class="author">
      <rect class="author-plate" x="268" y="1025" width="264" height="82"/>
      <text class="author-name" x="400" y="1083" text-anchor="middle">Ravi Menhar</text>
    </g>
  </svg>
</main>
</body>
</html>
```